Tova Brisk Fitness Coaching Project

I am a personal trainer based in London. My services include one-on-one PT sessions, bootcamps.
I would like the design to be minimalistic. With light colours: white, pink, purple.
I specialise in weight loss, flexibility, mobility.

Tova Penrick
Personal Trainer
Email: tova.penrick@mailgrove.net
tel: 07500 918 243
Instagram: Tova Brisk

Target Market(s)

adults, mostly females (age 18-50).

Industry/Entity Type

Fitness

Contact Information for Business Card

Tova Penrick
Personal Trainer
tel: 07500 918 243
Instagram: Tova Brisk

Font styles to use
Serif

Colors
eea4c8
fbd4d5
fdf9cf
cfeae6
cee9f5

Requirements
Nice to have
• minimalistic style
• easy to read and remember

```html
<!DOCTYPE html>
<html lang="en">
<head>
<meta charset="utf-8">
<title>Tova Penrick – Personal Trainer Card</title>
<link href="https://fonts.googleapis.com/css2?family=Libre+Baskerville:ital,wght@1,700&family=Cormorant+Garamond:wght@500&family=Marcellus+SC&display=swap" rel="stylesheet">
<style>
  :root {
    --paper: #ffffff;
    --band: #faf9c6;
    --ink-pink: #ec8ccb;
    --soft-pink: #fbd4d5;
    --soft-yellow: #fdf9cf;
    --soft-mint: #cfeae6;
    --soft-blue: #cee9f5;
  }
  * { margin: 0; padding: 0; box-sizing: border-box; }
  html, body { width: 1000px; height: 1200px; overflow: hidden; background: var(--paper); }
  .card {
    position: relative;
    width: 1000px;
    height: 1200px;
    background: var(--paper);
    overflow: hidden;
  }
  .card__pattern {
    position: absolute;
    left: 0; top: 0;
    width: 1000px; height: 600px;
    background:
      radial-gradient(circle at 15% 30%, rgba(251,212,213,0.55), transparent 45%),
      radial-gradient(circle at 80% 25%, rgba(206,233,245,0.55), transparent 45%),
      radial-gradient(circle at 55% 70%, rgba(207,234,230,0.5), transparent 45%),
      radial-gradient(circle at 35% 75%, rgba(253,249,207,0.7), transparent 40%),
      var(--paper);
  }
  .card__band {
    position: absolute;
    left: 0; top: 600px;
    width: 1000px; height: 600px;
    background: var(--band);
    text-align: center;
    color: var(--ink-pink);
  }
  .card__name {
    position: absolute;
    left: 0; right: 0; top: 100px;
    font-family: "Libre Baskerville", Georgia, serif;
    font-style: italic;
    font-weight: 700;
    font-size: 80px;
    line-height: 1;
    letter-spacing: 1px;
  }
  .card__role {
    position: absolute;
    left: 0; right: 0; top: 195px;
    font-family: "Cormorant Garamond", Georgia, serif;
    font-weight: 500;
    font-size: 38px;
    letter-spacing: 2px;
    line-height: 1;
  }
  .card__divider {
    position: absolute;
    left: 335px; top: 270px;
    width: 330px; height: 36px;
  }
  .contact {
    position: absolute;
    left: 0; right: 0; top: 330px;
    font-family: "Cormorant Garamond", Georgia, serif;
    font-weight: 500;
    font-size: 32px;
    line-height: 1;
  }
  .contact__item { height: 54px; display: flex; align-items: center; justify-content: center; }
  .contact__handle {
    font-family: "Marcellus SC", Georgia, serif;
    font-size: 28px;
    letter-spacing: 1.5px;
    gap: 10px;
  }
  .contact__dot {
    display: inline-block;
    width: 30px; height: 30px;
    border: 3px solid var(--ink-pink);
    border-radius: 50%;
  }
</style>
</head>
<body>
  <main class="card">
    <div class="card__pattern" role="img" aria-label="Hand-drawn pastel squiggles in pink, yellow, mint and blue scattered across a white background"></div>
    <section class="card__band">
      <h1 class="card__name">TOVA PENRICK</h1>
      <p class="card__role">PERSONAL TRAINER</p>
      <svg class="card__divider" viewBox="0 0 330 36" aria-hidden="true">
        <path d="M4 22 C 70 0, 130 8, 170 20 S 270 34, 326 8" fill="none" stroke="var(--soft-blue)" stroke-width="7" stroke-linecap="round"/>
      </svg>
      <div class="contact">
        <p class="contact__item">tova.penrick@mailgrove.net</p>
        <p class="contact__item contact__handle"><span class="contact__dot"></span>Tova Brisk</p>
        <p class="contact__item">+07500 918 243</p>
      </div>
    </section>
  </main>
</body>
</html>
```